terras letterhead

We would like to create a new letterhead that our company will use for proposals, invoices, statements and letters. Our company name is Terra-Crafters. We are a landscape design/build and landscape maintenance company. We have a web site Terra-Crafters.example where our logo (the leaf with the lettering within it only) is displayed.

Industry/Entity Type

Graphic Design

Requirements
Must have
• Address and info on our current letterhead (uploaded)
Nice to have
• We would like the design to look presentable in grey scale as well as color.
Should not have
• Do not want to infringe much on the normal useable area within the normal print areas.

```html
<!DOCTYPE html>
<html lang="en">
<head>
<meta charset="utf-8">
<title>Terra-Crafters Letterhead</title>
<link rel="stylesheet" href="https://fonts.googleapis.com/css2?family=Arimo:wght@400;700&display=swap">
<style>
  :root {
    --backdrop: #c6c6c6;
    --paper: #ffffff;
    --brand-green: #1f4a23;
    --contact-green: #0d3d10;
    --email-green: #1c6b1f;
    --web-grey: #333333;
  }
  * { margin: 0; padding: 0; box-sizing: border-box; }
  html, body {
    width: 848px;
    height: 1200px;
    overflow: hidden;
    background: var(--backdrop);
    font-family: "Arimo", Arial, sans-serif;
  }
  .letterhead {
    position: absolute;
    left: 161px;
    top: 194px;
    width: 550px;
    height: 777px;
    background: var(--paper);
  }
  .brand {
    position: absolute;
    right: 54px;
    top: 36px;
    display: flex;
    align-items: center;
    gap: 6px;
    color: var(--brand-green);
    font-size: 13px;
    font-weight: 700;
    letter-spacing: 0.3px;
  }
  .brand-dot {
    width: 10px;
    height: 10px;
    border-radius: 50%;
    background: var(--brand-green);
  }
  .contact-block {
    position: absolute;
    left: 374px;
    top: 659px;
    font-size: 12.5px;
    line-height: 16px;
    color: var(--contact-green);
  }
  .website {
    position: absolute;
    left: 50px;
    top: 733px;
    font-size: 12.5px;
    color: var(--web-grey);
  }
  .email {
    position: absolute;
    left: 374px;
    top: 733px;
    font-size: 12.5px;
    color: var(--email-green);
  }
</style>
</head>
<body>
  <main class="letterhead">
    <div class="brand">
      <span class="brand-dot"></span>
      <span class="brand-name">Terra-Crafters</span>
    </div>
    <address class="contact-block" style="font-style: normal;">
      1815 Meadowbrook Avenue,<br>
      Cedar Glen, NJ 07000<br>
      (555) 014-2210&nbsp; F<br>
      ax: (555) 014-2278
    </address>
    <p class="website">www.terra-crafters.example</p>
    <p class="email">Service@Terra-crafters.example</p>
  </main>
</body>
</html>
```